SaaS / Consulting / Solution website redesign

We need a website design that:
- Is completely different than our current design : https://brightlanehub.com
- Has a very minimal amount of copy
- Changes our positioning from a SaaS application to a solutions company. Solutions company means that we help our customers solve their problems with consulting, training, and tools. An example of a solutions company is here: https://pastpages.example/web/20130111103320/http://www.quorvex.com:80/
- Does not make us look like a start up
- Is more people oriented than technology oriented

We need a designer that:
- Is a rebel at heart
- Is a minimalist
- Tells us why our current site sucks
- Can disagree with us
- Can also do copywriting or already has a copywriter that can help
- Is ok with saying we have capability that we don't in order to see if people actually want that
- Can understand the difference between our grand vision and where we need to focus ourselves today in order to get there

Who we are:
- Entrepreneurs
- Programmers
- Consultants
- Investors

Here's our design goals:
#1 Get customers, investors, employers, and partners excited about our unique and clearly articulated value proposition
#2 Get people to contact us asking for help with their programs
#3 Position ourselves as an expert in the skills based volunteering, mentorship, and group collaboration
#4 Make it easy for people, who already know who we are, to register online

What our grand vision is:
- Create a marketplace where any person can go to our site and find time with anyone they need to meet with. Whether that is their hair stylist, school advisor, parent of your kids class, dentist, attorney, etc.

What will you get if you win:
- In addition to the prize of this project we will have many landing pages and other revisions we will need in the future. We currently don't have a designer or copywriter and need to add that capability to our team

Who do we need to appeal to:
- Directors that are launching innovative programs inside organizations
- IT personnel who are trying to disqualify our technology so they don't have to support it or deal with it when it doesn't go well
- Enterprise IT architects who don't want our product being on its own island within their organization totally incompatible with everything else. Architects which are trying to assess how our platform will co-exist with all their other platforms
- Vice Presidents who want to help their directors understand that we don't have enough experience to help them
- Program managers who have to juggle a million things and need a tool that actually helps instead of confuses them and adds more work for them.
- Program managers & directors that have been given ambiguous goals by their board of directors like "improve retention, increase engagement, create innovation, get people to collaborate." And who have no idea where to start or how to deliver on things like that.
- Program managers, directors, and vice presidents that are trying to understand how our technology and services fit into their existing technology and capability
- Employees who are bored and uninspired with their current tools and are hoping for some excitement in their life. Kind of like candy or a double espresso.
- Investors who think, our company like all the rest, are going to waste their money and make them look like a fool

Other information:
-The CSS and html needs to be responsive

-Our registration onboarding flow needs to collect this information:
User first name
user last name
user email
(verify their email)
user phone number
(verify their phone number)
User profile image (optional)
User profile summary (optional, like a bio, freeform text fiels)
If applicable: Register their organization
Organization name
Organization image (optional)
Account Mailing address
account Billing address (could be same as mailing address)
account Billing email address (could be same as user address)
account Product selection (pricing tier)
account Credit card information

The designs I am getting are a good start but they are only the front page. I just want you to know that I am expecting and need more than a landing page to complete the design. I will likely need a page that outlines the benefits and features of the product itself, how its different than our competitors, which will not be on the front page. I will need a registration flow. I will need a blog page design so we can post blog articles, I will need a team page, a page that goes into detail on our training, our services. I will likely need a page that shows all news and media we have been in. I need to show customer and user quotes, case studies, a way to contact us, partners, general resources like on collaboration, product tutorials, customers. I need the site to address a comprehensive set of needs. I need that design to be consistent and thorough. I know what LayoutBazaar is. I'm not using because I need more than a template that was customized. I need to be unique and match our brand thoughtfully, beautifully, and artistically. Someone asked me a question about how Murmo is similar to our tool in the way it is referred by end users and purchased by managers. Our website needs to primarily talk to the managers as I explained in the brief but it needs to appear cool and exciting to our end-users without focusing on the technology too much. Murmo is a tool that teams use to collaborate in small and large enterprises. The value prop for them is that communication is easier. But they don't put that on their website. Why? Because the users of the technology won't go to the website to find out information on it, they get their information from someone who is using it and demos it to them. When Lena tells her manager Tod "Lets get murmo, Ruth is using it at her company and its great" Lena's manager doesn't know anything about murmo so she promptly googles it. The most important thing from Lena's perspective is that Tod agrees to try it out. Tod's biggest concern is that productivity will be enhanced to degraded. Murmo knows this and so on the front page they know they are talking to Tod NOT Lena because Lena is already sold on it and doesn't need to get sold on the website. Lena is end user. Tod is the purchaser. We have the same problem and so our end users are not the ones purchasing our product, their managers are purchasing our product. We get referred by our end users and vetted by their managers. Hope this helps! Thank you for looking at this project!  Added Wednesday, June 7, 2017

Another observation I am having about the designs being submitted. I believe we used the animations on our current website because animations / cartoons connect with the "inner child" in our users. Whatever that means :-). I think it's what makes our brand fun. I have a hard time imagining that we could make the design fun looking without animations but I'm sure it can be achieved. I also recognize that blending pictures of real people and animations is hard. So either we must masterfully blend them, use only animations, or make the real people have a LOT of fun! So far most of the designs while achieve the goal of appealing to the serious Vice Presidents and directors, they are not doing a good job at appealing to the overworked program managers and bored employees. There seems to stand another challenge with animations which is animations are hard to find and/or create that achieve the message / emotion we are trying to communicate. I don't have any good answers for this but I will say we can hire both animators and illustrators if we need to. All you have to do is communicate the effect in the website design with some simpler version maybe not the end illustration or animation itself. Added Wednesday, June 7, 2017

• Sex appeal and a sense of humor. Copy that makes people excited and clairvoyant about our potential.
• Boring renditions of other non-inspiring websites

```html
<!DOCTYPE html>
<html lang="en">
<head>
<meta charset="utf-8">
<title>BrightLane — Contact Us</title>
<link href="https://fonts.googleapis.com/css2?family=Raleway:wght@400;500;600&display=swap" rel="stylesheet">
<style>
  :root {
    --sky: #3db5e6;
    --leaf: #7fcc85;
    --ink: #2b2b2b;
    --muted: #b8b8b8;
    --line: #cfcfcf;
    --night: #30323d;
    --paper: #ffffff;
  }
  * { box-sizing: border-box; margin: 0; padding: 0; }
  html, body {
    width: 1200px; height: 912px; overflow: hidden;
    background: var(--paper);
    font-family: "Raleway", Arial, sans-serif;
    color: var(--ink);
  }
  .page { position: relative; width: 1200px; height: 912px; }

  .site-header {
    position: absolute; left: 123px; top: 0; width: 949px; height: 64px;
    background: var(--paper);
    border-radius: 0 0 33px 33px;
    box-shadow: 0 2px 4px rgba(0,0,0,0.18);
    z-index: 2;
  }
  .brand {
    position: absolute; left: 58px; top: 18px;
    display: flex; align-items: center; gap: 6px;
    font-size: 16px; font-weight: 600; color: var(--leaf);
  }
  .brand-dot {
    width: 18px; height: 18px; border-radius: 50%;
    border: 2px solid var(--leaf);
  }
  .main-nav {
    position: absolute; top: 24px; left: 0; width: 100%;
    font-size: 11.7px; letter-spacing: 0.3px;
  }
  .main-nav a { position: absolute; color: var(--ink); text-decoration: none; }

  .contact-tab {
    position: absolute; left: 459px; top: 56px; width: 283px; height: 62px;
    background: var(--sky); color: var(--paper);
    border-radius: 0 0 26px 26px;
    display: flex; align-items: flex-end; justify-content: center;
    padding-bottom: 15px;
    font-size: 20px; font-weight: 400; letter-spacing: 0.3px;
  }
  .contact-intro {
    position: absolute; top: 145px; width: 100%;
    text-align: center; font-size: 11.7px;
  }

  .contact-form .field {
    position: absolute; left: 425px; width: 350px;
    border: 1px solid var(--line); border-radius: 4px;
    padding: 0 24px; font-size: 11.7px; color: var(--muted);
    display: flex; align-items: center;
  }
  .field-name { top: 197px; height: 50px; }
  .field-email { top: 262px; height: 50px; }
  .field-message { top: 327px; height: 127px; align-items: flex-start !important; padding-top: 18px !important; }
  .send-button {
    position: absolute; left: 425px; top: 483px; width: 350px; height: 50px;
    background: var(--sky); color: var(--paper);
    border-radius: 4px; font-size: 15px;
    display: flex; align-items: center; justify-content: center;
  }

  .site-footer {
    position: absolute; left: 0; top: 617px; width: 1200px; height: 295px;
    background: var(--night); border-radius: 46px 46px 0 0;
    color: var(--paper);
  }
  .footer-brand {
    position: absolute; left: 207px; top: 128px;
    display: flex; align-items: center; gap: 12px;
    font-size: 36px; font-weight: 600; color: var(--leaf);
  }
  .footer-brand .brand-dot { width: 40px; height: 40px; border-width: 3px; }
  .footer-links {
    position: absolute; right: 452px; top: 120px;
    list-style: none; text-align: right; font-size: 12.5px; line-height: 19.8px;
  }
  .footer-divider {
    position: absolute; left: 762px; top: 113px; width: 1px; height: 90px;
    background: var(--sky);
  }
  .footer-contact {
    position: absolute; left: 774px; top: 120px;
    display: grid; grid-template-columns: 92px auto;
    font-size: 12.5px; line-height: 19.8px;
  }
</style>
</head>
<body>
<div class="page">
  <header class="site-header">
    <div class="brand"><span class="brand-dot"></span>BrightLane</div>
    <nav class="main-nav">
      <a href="#" style="left:540px">INDUSTRIES</a>
      <a href="#" style="left:656px">CUSTOMERS</a>
      <a href="#" style="left:774px">ABOUT</a>
      <a href="#" style="left:862px">LOGIN</a>
    </nav>
  </header>

  <div class="contact-tab">CONTACT US</div>
  <p class="contact-intro">We'd love to learn more about you</p>

  <form class="contact-form">
    <div class="field field-name">Name</div>
    <div class="field field-email">Email</div>
    <div class="field field-message">Message</div>
    <div class="send-button">Send Message</div>
  </form>

  <footer class="site-footer">
    <div class="footer-brand"><span class="brand-dot"></span>BrightLane</div>
    <ul class="footer-links">
      <li>Industries</li>
      <li>Customers</li>
      <li>About</li>
      <li>Login</li>
    </ul>
    <div class="footer-divider"></div>
    <div class="footer-contact">
      <span>Address:</span><span>brightlane.example</span>
      <span>Phone:</span><span>+10555014782</span>
      <span>Email:</span><span>info@brightlane.example</span>
      <span>Fax:</span><span>+10 555 019-2600</span>
    </div>
  </footer>
</div>
</body>
</html>
```